Merrowind Winery Wine Label Re-design

Merrowind Winery is located in the Finger Lakes region of New York. The Calloway Family planted the first vineyards in 1979 and opened in 1986. We produce award winning premium, hand crafted estate grown wines. We are in the process of a wine label re-design across our entire line. We would like to have the new label 'pop' but still convey elegance and ultra-premium quality. We are open to all color and styles or a minimalist design.
The attached files contain our new logo and samples of our current label (marked current) with dimensions. Our labeler is limited to label shapes but does not necessarily to have to be die-cut(the top arch) like our current label.

Target Market(s)

Upper income quality wine drinkers

Colors

Designer to choose colors to be used in the design.

Requirements
Should not have
• Should not be a tranparent label

```html
<!DOCTYPE html>
<html lang="en">
<head>
<meta charset="utf-8">
<title>Merrowind Winery – Chardonnay Label</title>
<link rel="stylesheet" href="https://fonts.googleapis.com/css2?family=Cinzel:wght@400&family=Libre+Baskerville:wght@700&family=Montserrat:wght@300;400&display=swap">
<style>
  :root {
    --plum: #4a1a33;
    --plum-deep: #3a1228;
    --gold: #b8902e;
    --ink: #2b2b2b;
    --paper: #ffffff;
  }
  html, body {
    margin: 0;
    padding: 0;
    width: 1200px;
    height: 922px;
    overflow: hidden;
    background: var(--paper);
  }
  .canvas {
    position: relative;
    width: 1200px;
    height: 922px;
  }
  .label {
    position: absolute;
    left: 320px;
    top: 45px;
    width: 560px;
    height: 832px;
  }
  .label__frame {
    position: absolute;
    inset: 0;
  }
  .label__seal {
    position: absolute;
    left: 242px;
    top: 54px;
    width: 76px;
    height: 76px;
    border: 3px solid var(--plum);
    border-radius: 50%;
    box-sizing: border-box;
  }
  .label__brand,
  .label__varietal,
  .label__note,
  .label__vintage {
    position: absolute;
    left: 0;
    right: 0;
    margin: 0;
    text-align: center;
    line-height: 1;
    white-space: nowrap;
  }
  .label__brand--name {
    top: 166px;
    font-family: "Cinzel", serif;
    font-weight: 400;
    font-size: 46px;
    letter-spacing: 0.2em;
    padding-left: 0.2em;
    color: var(--plum);
  }
  .label__brand--sub {
    top: 214px;
    font-family: "Montserrat", sans-serif;
    font-weight: 300;
    font-size: 23px;
    letter-spacing: 0.7em;
    padding-left: 0.7em;
    color: var(--plum);
  }
  .label__artwork {
    position: absolute;
    left: 124px;
    top: 248px;
    width: 312px;
    height: 405px;
    border-radius: 48% 48% 45% 45% / 40% 40% 60% 60%;
    background:
      radial-gradient(circle at 50% 68%, rgba(201,96,110,0.85) 0%, rgba(201,96,110,0.35) 38%, transparent 60%),
      radial-gradient(circle at 30% 30%, rgba(199,154,74,0.55) 0%, transparent 45%),
      radial-gradient(circle at 72% 38%, rgba(169,170,166,0.7) 0%, transparent 50%),
      linear-gradient(180deg, #efe3dc 0%, #ead1d2 60%, #e2c9b8 100%);
  }
  .label__varietal {
    top: 697px;
    font-family: "Libre Baskerville", serif;
    font-weight: 700;
    font-size: 33px;
    color: var(--plum-deep);
  }
  .label__note {
    top: 732px;
    font-family: "Montserrat", sans-serif;
    font-weight: 400;
    font-size: 17px;
    letter-spacing: 0.03em;
    word-spacing: 0.3em;
    color: var(--ink);
  }
  .label__vintage {
    top: 756px;
    font-family: "Libre Baskerville", serif;
    font-weight: 700;
    font-size: 31px;
    color: var(--gold);
  }
</style>
</head>
<body>
<main class="canvas">
  <section class="label" aria-label="Merrowind Winery Chardonnay wine label">
    <svg class="label__frame" width="560" height="832" viewBox="0 0 560 832" aria-hidden="true">
      <path d="M1,200 Q1,150 50,145 L110,140 Q150,135 160,100 Q180,8 280,3 Q380,8 400,100 Q410,135 450,140 L510,145 Q559,150 559,200 L559,780 Q559,829 512,829 L48,829 Q1,829 1,780 Z"
            fill="#ffffff" stroke="var(--plum)" stroke-width="2"/>
      <path d="M18,215 Q18,168 62,163 L112,158 Q165,152 176,112 Q195,26 280,21 Q365,26 384,112 Q395,152 448,158 L498,163 Q542,168 542,215 L542,770 Q542,810 502,810 L58,810 Q18,810 18,770 Z"
            fill="none" stroke="var(--plum)" stroke-width="7"/>
    </svg>

    <div class="label__seal" aria-hidden="true"></div>
    <p class="label__brand label__brand--name">MERROWIND</p>
    <p class="label__brand label__brand--sub">WINERY</p>

    <div class="label__artwork" role="img" aria-label="Engraved-style illustration of a grape cluster with vine leaves and tendril in rose, grey and gold tones"></div>

    <h1 class="label__varietal">CHARDONNAY</h1>
    <p class="label__note">ESTATE GROWN &amp; BOTTLED</p>
    <p class="label__vintage">2014</p>
  </section>
</main>
</body>
</html>
```